Accountant and Financial Advisor Client Presentation Folder

We are a medium sized accountancy / taxation and financial advisory firm who has just been through the process of obtaining a new logo and updating our stationary. The last piece of the puzzle is to redesign our existing client presentation folder so that it fits with our new logo (which is black and green).

We want a modern unique image, something creative, but remain professional. Also portray integrity and look approachable. We want to appeal to the younger generation while not losing the respect of our more conservative older clients.

The necessary words and logo to be included on the folder are attached (Presentation Folder Brief), the overall design of the folder is up to you.
We want our new folder to look attractive and stand out from the crowd preferably with a graphic. We have included our old folder which we like (has the dandelion) however the colours etc have now changed as per the black and green mock-up folder example.
We would like a redesign so that we have a graphic to break up the colour. We are open to design changes on the shape of the folder.

Target Market(s)

younger generation while not losing the respect of our more conservative older clients

Industry/Entity Type

Financial

Requirements
Must have
• Graphic in the folder Design

```html
<!DOCTYPE html>
<html lang="en">
<head>
<meta charset="utf-8">
<title>Clear Ledger – Presentation Folder</title>
<link href="https://fonts.googleapis.com/css2?family=Montserrat:wght@500;600;700&family=Open+Sans:wght@400;700&display=swap" rel="stylesheet">
<style>
  :root {
    --lime: #a3d80a;
    --lime-deep: #86b00a;
    --lime-light: #b4e23a;
    --band: #95c21c;
    --charcoal: #202020;
    --white: #ffffff;
    --ink-soft: #4a4a4a;
  }
  * { margin: 0; padding: 0; box-sizing: border-box; }
  html, body { width: 1200px; height: 822px; overflow: hidden; background: var(--white); }
  .folder { position: relative; width: 1200px; height: 822px; }
  .dieline { position: absolute; inset: 0; }
  .intro {
    position: absolute; left: 640px; top: 20px; width: 225px;
    font: 400 8.2px/12px "Open Sans", sans-serif; color: var(--white); text-align: right;
  }
  .intro strong { font-weight: 700; }
  .intro .intro-name { color: var(--ink-soft); }
  .headline {
    position: absolute; left: 490px; top: 206px;
    font: 700 23px/22.5px "Montserrat", sans-serif; color: var(--white); text-transform: uppercase;
  }
  .brand {
    position: absolute; left: 916px; top: 386px;
    display: flex; align-items: center; gap: 8px;
  }
  .brand-mark { width: 12px; height: 12px; background: var(--lime); }
  .brand-name { font: 700 20px/1 "Montserrat", sans-serif; color: var(--lime); }
  .brand-tag {
    position: absolute; left: 916px; top: 424px;
    font: 600 4.4px/1 "Montserrat", sans-serif; color: var(--white); text-transform: uppercase;
  }
  .firm-type {
    position: absolute; left: 916px; top: 438px;
    font: 500 9.6px/11px "Montserrat", sans-serif; color: var(--white);
  }
  .contact {
    position: absolute; left: 916px; top: 512px;
    font: 400 6px/8.2px "Open Sans", sans-serif; color: var(--white);
  }
  .contact .label { color: var(--lime); font-weight: 700; }
  .web {
    position: absolute; left: 916px; top: 565px;
    font: 700 8px/1 "Open Sans", sans-serif; color: var(--lime);
  }
  .services {
    position: absolute; left: 700px; top: 624px; width: 141px;
    font: 500 9px/11px "Montserrat", sans-serif; color: var(--white);
    text-transform: uppercase; text-align: left; transform: rotate(180deg);
  }
</style>
</head>
<body>
<div class="folder">
  <svg class="dieline" width="1200" height="822" viewBox="0 0 1200 822">
    <defs>
      <clipPath id="flap-clip">
        <polygon points="878,10 916,10 1088,152 1200,236 1152,368 1072,605 878,605"/>
      </clipPath>
      <linearGradient id="family-field" x1="0" y1="0" x2="0" y2="1">
        <stop offset="0" stop-color="#e9e4d8"/><stop offset="0.55" stop-color="#cfc3a0"/><stop offset="1" stop-color="#8ea440"/>
      </linearGradient>
      <linearGradient id="coin-seedling" x1="0" y1="0" x2="1" y2="1">
        <stop offset="0" stop-color="#dfe3ea"/><stop offset="0.5" stop-color="#7aa23a"/><stop offset="1" stop-color="#c9a583"/>
      </linearGradient>
      <linearGradient id="retirees" x1="0" y1="0" x2="1" y2="1">
        <stop offset="0" stop-color="#f2efea"/><stop offset="0.6" stop-color="#cdb9a5"/><stop offset="1" stop-color="#9c8a7a"/>
      </linearGradient>
      <linearGradient id="hedge-arrow" x1="0" y1="0" x2="0" y2="1">
        <stop offset="0" stop-color="#a3d80a"/><stop offset="0.35" stop-color="#5d8f2a"/><stop offset="1" stop-color="#4f8a22"/>
      </linearGradient>
    </defs>

    <!-- inside left panel -->
    <rect x="0" y="0" width="444" height="614" fill="var(--lime)"/>
    <polygon points="146,0 444,0 444,152 230,152 146,152" fill="var(--lime-deep)"/>
    <polygon points="230,152 416,0 444,0 444,8 255,152" fill="var(--lime-light)" opacity="0.5"/>
    <polygon points="0,560 170,374 380,374 80,614 0,614" fill="var(--lime-light)" opacity="0.55"/>
    <line x1="170" y1="374" x2="250" y2="605" stroke="var(--white)" stroke-width="0.8" opacity="0.8"/>
    <rect x="0" y="152" width="444" height="12" fill="var(--band)"/>
    <rect x="0" y="364" width="444" height="10" fill="var(--band)"/>
    <rect x="10" y="164" width="144" height="200" fill="url(#family-field)" role="img" aria-label="Photo: young family running through a sunny meadow"/>
    <rect x="156" y="164" width="142" height="200" fill="url(#coin-seedling)" role="img" aria-label="Photo: cupped hands holding coins with a green seedling"/>
    <rect x="300" y="164" width="144" height="200" fill="url(#retirees)" role="img" aria-label="Photo: retired couple reviewing finances at home"/>

    <!-- front cover -->
    <rect x="444" y="0" width="434" height="605" fill="var(--lime)"/>
    <rect x="444" y="368" width="434" height="237" fill="url(#hedge-arrow)" role="img" aria-label="Illustration: hedge grown into a rising arrow chart on a grass field"/>

    <!-- right flap -->
    <polygon points="878,10 916,10 1088,152 1200,236 1152,368 1072,605 878,605" fill="var(--charcoal)"/>
    <g clip-path="url(#flap-clip)">
      <rect x="878" y="152" width="322" height="12" fill="var(--band)"/>
      <rect x="878" y="364" width="322" height="10" fill="var(--band)"/>
      <rect x="878" y="164" width="144" height="200" fill="url(#family-field)" role="img" aria-label="Photo: young family running through a sunny meadow"/>
      <rect x="1024" y="164" width="144" height="200" fill="url(#coin-seedling)" role="img" aria-label="Photo: cupped hands holding coins with a green seedling"/>
      <rect x="1170" y="164" width="30" height="200" fill="url(#retirees)" role="img" aria-label="Photo: retired couple reviewing finances"/>
    </g>

    <!-- bottom pocket -->
    <rect x="436" y="605" width="452" height="217" fill="var(--charcoal)"/>

    <!-- cut and fold lines -->
    <g fill="none" stroke="var(--white)" stroke-width="0.8" stroke-dasharray="3 2" opacity="0.85">
      <polyline points="10,10 444,10 444,605 10,605 10,10"/>
      <line x1="444" y1="10" x2="878" y2="10"/>
      <polyline points="878,605 878,692 444,812 444,605"/>
      <rect x="482" y="627" width="171" height="104"/>
      <line x1="478" y1="640" x2="498" y2="622"/>
      <line x1="638" y1="736" x2="658" y2="718"/>
    </g>
  </svg>

  <p class="intro">
    <strong class="intro-name">Clear Ledger</strong> is a results-focused
    <strong>Accounting, Taxation and Financial Advisory firm</strong> that integrates your personal, business and
    financial needs in the interests of better outcomes for you. We see ourselves as a professional
    advisor for life, able to deliver complete <strong>financial solutions</strong> that considers
    <strong>tax, business, superannuation, retirement</strong> and <strong>investment planning</strong> proactively.
  </p>

  <h1 class="headline">Build<br>your<br>business &amp;<br>grow<br>your<br>wealth</h1>

  <div class="brand"><span class="brand-mark"></span><span class="brand-name">Clear Ledger</span></div>
  <p class="brand-tag">Build your business &amp; grow your wealth</p>
  <p class="firm-type">Accounting, Taxation and<br>Financial Advisory Firm</p>
  <p class="contact">
    Suite 4 / 118 Harbour View Road<br>
    PO Box 1420, Bayfield NSW 2261<br>
    <span class="label">P</span> : (02) 5550 1234<br>
    <span class="label">E</span> : info@clearledger.example
  </p>
  <p class="web">www.clearledger.example</p>

  <p class="services">Self managed super funds<br>Financial advice<br>Tax agents<br>Accounting</p>
</div>
</body>
</html>
```